Promotional Ruler Graphic Design

We are going to give away a 12" ruler at an upcoming trade show. The center of the ruler has an imprint area of 11.2 inches wide by 1.0 inches high (plus a bleed area). We are looking for a 4-color graphic to go in that space that will summarize who we are, what we do, and how to contact us. The actual body of the ruler itself is red with white markings and our company colors are red, white, and black. If you visit our website (www.vorlamqs.com) you will get a feel for our overall brand and how we are focused on the healthcare industry. I have attached a gimp file that is a rough outline of what we need, but I'm looking for graphical variations on the theme and more creative backgrounds and use of color. I've also attached some other art work that might be of help in composing the solution.

```html
<!DOCTYPE html>
<html lang="en">
<head>
<meta charset="utf-8">
<title>Vorlamq Systems – Ruler Imprint</title>
<link rel="stylesheet" href="https://fonts.googleapis.com/css2?family=Arvo:wght@700&family=Arimo:wght@400&display=swap">
<style>
  :root {
    --ink-black: #070707;
    --deep-maroon: #3a0508;
    --brand-red: #c4161c;
    --bright-red: #e2262c;
    --glow-rose: #f2b9b6;
    --panel-white: #ffffff;
    --headline-white: #ffffff;
    --contact-grey: #f0e2e2;
  }
  html, body {
    margin: 0;
    padding: 0;
    overflow: hidden;
    background: #ffffff;
  }
  .ruler-imprint {
    position: relative;
    width: 1200px;
    height: 112px;
    overflow: hidden;
    background: linear-gradient(90deg, var(--ink-black) 0%, var(--deep-maroon) 24%, var(--brand-red) 52%, var(--deep-maroon) 76%, var(--ink-black) 100%);
  }
  .earth-scene {
    position: absolute;
    left: 240px;
    top: 0;
    width: 620px;
    height: 112px;
    background:
      radial-gradient(ellipse 340px 150px at 200px 140px, rgba(226,38,44,0.85), rgba(226,38,44,0) 72%),
      radial-gradient(ellipse 200px 70px at 470px 20px, rgba(242,185,182,0.35), rgba(242,185,182,0) 75%);
  }
  .headset-portrait {
    position: absolute;
    right: 0;
    top: 0;
    width: 320px;
    height: 112px;
    background:
      radial-gradient(ellipse 150px 80px at 110px 40px, rgba(242,185,182,0.55), rgba(242,185,182,0) 72%),
      linear-gradient(90deg, rgba(7,7,7,0) 0%, rgba(7,7,7,0.6) 60%, var(--ink-black) 100%);
  }
  .brand-panel {
    position: absolute;
    left: 22px;
    top: 20px;
    width: 235px;
    height: 80px;
    background: var(--panel-white);
    display: flex;
    align-items: center;
    justify-content: center;
  }
  .brand-name {
    font-family: "Arvo", Georgia, serif;
    font-weight: 700;
    font-size: 25px;
    color: var(--brand-red);
  }
  .headline {
    position: absolute;
    left: 394px;
    top: 46px;
    width: 520px;
    margin: 0;
    font-family: "Arvo", Georgia, serif;
    font-weight: 700;
    font-size: 32px;
    line-height: 1;
    letter-spacing: -0.6px;
    color: var(--headline-white);
    white-space: nowrap;
    text-shadow: 0 1px 2px rgba(0,0,0,0.6);
  }
  .contact-line {
    position: absolute;
    left: 601px;
    top: 86px;
    margin: 0;
    font-family: "Arimo", Arial, sans-serif;
    font-size: 12px;
    line-height: 1;
    color: var(--contact-grey);
    letter-spacing: 0.3px;
    white-space: nowrap;
  }
  .contact-line .phone {
    margin-left: 22px;
  }
</style>
</head>
<body>
  <div class="ruler-imprint">
    <div class="earth-scene" role="img" aria-label="Earth seen from space"></div>
    <div class="headset-portrait" role="img" aria-label="Woman wearing a telephone headset"></div>
    <div class="brand-panel">
      <span class="brand-name">Vorlamq Systems</span>
    </div>
    <h1 class="headline">Advanced Voice &amp; Data Solutions</h1>
    <p class="contact-line"><span class="web">www.vorlamqs.com</span><span class="phone">866-555-0148</span></p>
  </div>
</body>
</html>
```